VentureListingsHubNow.com - website
Business Opportunity website
VentureListingsHubNow.com - website - Advertising
Creative Brief
Advertising
We are an advertising site that lists available business opportunities. Advertisers pay us to post their opportunities and visitors can view, contact business opportunities.
http://www.tradeploverlink.example/
http://www.marketventurely.example/
-Listings to be displayed in 4 columns like uploaded image example. -Cart Form for requesting info... up to 10 opportunities at a time. -3 search fields: 1/ industry 2/ price 3/ location - navigation 1/Home 2/ Advertise 3/ Contact - navigation bottom 1/Home 2/ Advertise 3/ Contact 4/ Privacy - Prospect Lantern Bulletin

```html
<!DOCTYPE html>
<html lang="en">
<head>
<meta charset="utf-8">
<title>VentureListingsHubNow.com</title>
<link href="https://fonts.googleapis.com/css2?family=Arimo:wght@400;700&display=swap" rel="stylesheet">
<style>
:root{
  --bar:#37331c;
  --bar-line:#5a5430;
  --search:#4b3a22;
  --search-dark:#2e2414;
  --page:#ece8dc;
  --white:#ffffff;
  --green:#6d8a2a;
  --red:#c4231c;
  --text:#333333;
  --muted:#666666;
  --border:#d8d3c4;
  --orange:#f0881c;
  --yellow:#f3d21b;
  --panel:#2b2a22;
  --footer:#16150f;
  --blue:#1f5fa8;
}
*{box-sizing:border-box;margin:0;padding:0}
html,body{width:1200px;height:1025px;overflow:hidden}
body{background:var(--page);font-family:"Arimo",Arial,sans-serif;color:var(--text);position:relative}
.topbar{position:absolute;top:0;left:0;width:1200px;height:38px;background:var(--bar);border-bottom:2px solid var(--bar-line)}
.topbar .nav{position:absolute;left:230px;top:0;display:flex;height:38px}
.topbar .nav a{color:#fff;font-size:13px;font-weight:700;text-decoration:none;padding:0 22px;line-height:38px}
.topbar .nav a.active{background:#58522c}
.newsletter{position:absolute;right:165px;top:8px;display:flex;align-items:center;gap:6px;font-size:11px;color:#ddd}
.newsletter .field{width:130px;height:21px;background:#fff;border:1px solid #999;font-size:10px;color:#999;padding:4px 6px}
.newsletter .go{height:21px;padding:0 10px;background:#8a8468;color:#fff;font-size:10px;line-height:21px}
.header{position:absolute;top:40px;left:167px;width:868px;height:120px;background:var(--white)}
.brand{position:absolute;left:22px;top:36px;display:flex;align-items:center;gap:9px;z-index:1;white-space:nowrap}
.brand .dot{width:24px;height:24px;border-radius:50%;background:var(--orange);flex:none}
.brand .name{font-size:21px;font-weight:700;color:var(--blue)}
.hero{position:absolute;right:0;top:0;width:470px;height:120px;background:linear-gradient(90deg,#ffffff 0%,#e7d4cf 15%,#b0423a 50%,#8c2a22 78%,#d7b2a6 100%)}
.search{position:absolute;top:160px;left:167px;width:868px;height:85px;background:linear-gradient(180deg,var(--search) 0%,var(--search-dark) 100%)}
.search h2{position:absolute;left:40px;top:12px;color:#fff;font-size:20px;font-weight:700}
.search .row{position:absolute;left:0;top:46px;width:868px;display:flex;align-items:center;justify-content:center;gap:8px;font-size:12px;font-weight:700;color:#fff}
.search .sel{width:130px;height:19px;background:#fff;border:1px solid #888;color:#666;font-size:10px;font-weight:400;padding:3px 5px;margin-right:22px}
.search .btn{height:19px;padding:0 8px;background:#ddd;color:#222;border:1px solid #888;font-size:10px;font-weight:400;line-height:17px}
.main{position:absolute;top:245px;left:167px;width:868px;height:650px;background:var(--white)}
.intro{position:absolute;left:23px;top:10px;width:820px;font-size:10.5px;line-height:14px;color:var(--green)}
.grid{position:absolute;left:23px;top:60px;width:560px;display:grid;grid-template-columns:repeat(4,132px);gap:14px 10px}
.card{height:262px;border:1px solid var(--border);padding:8px 10px;font-size:9.5px;line-height:12px}
.card .req{display:flex;align-items:center;gap:5px;font-size:10px;margin-bottom:6px}
.box{width:11px;height:11px;border:1px solid #777;background:#fff;display:inline-block}
.card .badge{height:52px;margin:0 4px 8px;border:1px solid #ccc}
.card h3{color:var(--red);font-size:10px;text-align:center;margin-bottom:4px}
.card p{color:var(--muted);margin-bottom:10px}
.card p .more{color:var(--red)}
.card .inv{text-align:center;color:var(--text)}
.panel{position:absolute;left:598px;top:60px;width:258px;height:575px;background:#f4f2ea;border:1px solid var(--border)}
.panel .head{background:var(--panel);color:#fff;padding:10px;font-size:10px;line-height:13px}
.panel .head h2{font-size:15px;margin-bottom:6px}
.panel .count{font-size:10px;color:#ddd;margin-top:6px}
.panel .list{margin:8px 10px;background:#000;color:var(--yellow);font-size:11px;font-weight:700;text-align:center;padding:14px 4px;border:1px solid #555}
.panel .req-note{color:var(--red);font-size:9px;font-weight:700;padding:2px 10px 6px}
.form{padding:0 10px;font-size:10px;font-weight:700}
.form .f{display:flex;align-items:center;justify-content:flex-end;gap:6px;margin-bottom:8px}
.form .in{width:160px;height:17px;border:1px solid #aaa;background:#fff;font-weight:400;font-size:9px;color:#999;padding:2px 4px}
.form .half{width:77px}
.form .submit{margin:10px 0 10px auto;width:58px;height:20px;background:var(--orange);color:#fff;font-size:10px;text-align:center;line-height:20px}
.checks{padding:0 10px;font-size:9px;line-height:12px;font-weight:400}
.checks div{display:flex;gap:5px;margin-bottom:6px}
.checks .box{flex:none;margin-top:1px}
.footer{position:absolute;top:895px;left:0;width:1200px;height:130px;background:var(--footer)}
.footer .links{position:absolute;left:190px;top:22px;color:#fff;font-size:12px;font-weight:700;word-spacing:6px}
.footer .copy{position:absolute;left:190px;top:55px;color:#777;font-size:10px}
</style>
</head>
<body>
<div class="topbar">
  <div class="nav"><a class="active">Home</a><a>Advertise</a><a>Contact</a></div>
  <div class="newsletter">Prospect Lantern Bulletin <span class="field">Email Address</span><span class="go">Join</span></div>
</div>

<div class="header">
  <div class="hero" role="img" aria-label="Photo of a cheering crowd raising hands in celebration"></div>
  <div class="brand"><span class="dot"></span><span class="name">VentureListingsHubNow.com</span></div>
</div>

<div class="search">
  <h2>Search Fields:</h2>
  <div class="row">
    <span>Industry:</span><span class="sel">Any</span>
    <span>Price:</span><span class="sel">Any</span>
    <span>location:</span><span class="sel">Any</span>
    <span class="btn">Search</span>
  </div>
</div>

<div class="main">
  <p class="intro">VentureListingsHubNow.com is a leading source for finding business opportunities, franchises for sale, business opportunities and small businesses. Browse our listings, request details from many sellers at once, and let our team guide you toward the right opportunity for your goals.</p>

  <div class="grid">
    <div class="card"><div class="req"><span class="box"></span>Request Info</div><div class="badge" style="background:#b92a22"></div><h3>Crimson Step Shoes</h3><p>Over a Century ago, Crimson Step Shoe Company was founded on a simple idea create work shoes and boots ... <span class="more">more</span></p><div class="inv">Investment:<br>$75,000 - $3,000,000</div></div>
    <div class="card"><div class="req"><span class="box"></span>Request Info</div><div class="badge" style="background:#1d4f9c"></div><h3>Quick Banner Signs</h3><p>Over a Century ago, Quick Banner Sign Company was founded on a simple idea create bold signs ... <span class="more">more</span></p><div class="inv">Investment:<br>$75,000 - $3,000,000</div></div>
    <div class="card"><div class="req"><span class="box"></span>Request Info</div><div class="badge" style="background:#f2c21c"></div><h3>Sandal Stop Shoes</h3><p>Over a Century ago, Sandal Stop Shoe Company was founded on a simple idea create beach shoes ... <span class="more">more</span></p><div class="inv">Investment:<br>$75,000 - $3,000,000</div></div>
    <div class="card"><div class="req"><span class="box"></span>Request Info</div><div class="badge" style="background:#e8eef4"></div><h3>Brushline Painters</h3><p>Over a Century ago, Brushline Painting Company was founded on a simple idea create fine homes ... <span class="more">more</span></p><div class="inv">Investment:<br>$75,000 - $3,000,000</div></div>
    <div class="card"><div class="req"><span class="box"></span>Request Info</div><div class="badge" style="background:#f3e7d0"></div><h3>Ledger Relief Advisors</h3><p>Over a Century ago, Ledger Relief Company was founded on a simple idea to help clients and families ... <span class="more">more</span></p><div class="inv">Investment:<br>$75,000 - $3,000,000</div></div>
    <div class="card"><div class="req"><span class="box"></span>Request Info</div><div class="badge" style="background:#2a2a2a"></div><h3>Sweet Stem Bouquet</h3><p>Over a Century ago, Sweet Stem Bouquet Company was founded on ... <span class="more">more</span></p><div class="inv">Investment:<br>$75,000 - $3,000,000</div></div>
    <div class="card"><div class="req"><span class="box"></span>Request Info</div><div class="badge" style="background:#6a2c8e"></div><h3>Shade &amp; Mat Works</h3><p>Over a Century ago, Shade Mat Company was founded on a simple idea create mats ... <span class="more">more</span></p><div class="inv">Investment:<br>$75,000 - $3,000,000</div></div>
    <div class="card"><div class="req"><span class="box"></span>Request Info</div><div class="badge" style="background:#e9a62a"></div><h3>Bright Canvas Coaching</h3><p>Over a Century ago, Bright Canvas Company was founded on a simple idea coach owners ... <span class="more">more</span></p><div class="inv">Investment:<br>$75,000 - $3,000,000</div></div>
  </div>

  <aside class="panel">
    <div class="head">
      <h2>Request More Information</h2>
      Complete the contact form below to review more information about the franchises you have selected.
      <div class="count">Selected Companies: 0 of 10</div>
    </div>
    <div class="list">Your Franchise Request List is Empty...</div>
    <div class="req-note">ALL FIELDS REQUIRED</div>
    <div class="form">
      <div class="f">Name:<span class="in half">First Name</span><span class="in half">Last Name</span></div>
      <div class="f">Email:<span class="in">Email Address</span></div>
      <div class="f">Phone:<span class="in">Phone Number</span></div>
      <div class="f">Address:<span class="in">Street Address</span></div>
      <div class="f">City:<span class="in"></span></div>
      <div class="f">State:<span class="in">- Select Your State -</span></div>
      <div class="f">Country:<span class="in">United States</span></div>
      <div class="f">Zip Code:<span class="in"></span></div>
      <div class="f">Capital:<span class="in">- Select Capital -</span></div>
      <div class="f">Timeframe:<span class="in">Immediately</span></div>
      <div class="submit">Submit</div>
    </div>
    <div class="checks">
      <div><span class="box"></span>Check here if you would like to receive the Prospect Lantern Bulletin on franchises and opportunities.</div>
      <div><span class="box"></span>Yes, I agree with the Terms &amp; Conditions</div>
    </div>
  </aside>
</div>

<div class="footer">
  <div class="links">Home | Advertise | Contact | Privacy</div>
  <div class="copy">Copyright 2010, VentureListingsHubNow.com. All rights reserved.</div>
</div>
</body>
</html>
```